Mother's Day Sale Banner Ad For Jewelry Site

We are looking for a designer to design a banner on our website advertising our Mother's Day Sale. I have enclosed a few pieces of jewelry we would like used in the ad. The ad size needs to be 1187 × 400. The ad should say:

Mother's Day Sale - Save 15% with Promo Code: LOVEMOM

Industry/Entity Type

Jewelry

```html
<!DOCTYPE html>
<html lang="en">
<head>
<meta charset="UTF-8">
<title>Mother's Day Sale</title>
<link href="https://fonts.googleapis.com/css2?family=Montserrat:wght@500&family=Raleway:wght@500;600&family=Josefin+Sans:wght@300&display=swap" rel="stylesheet">
<style>
  :root {
    --cream-light: #fdfbf1;
    --cream: #f7efd3;
    --cream-deep: #efe2b6;
    --band: #f1e4b5;
    --maroon: #8a3247;
    --rule: #7c2a3c;
    --ink: #2f2f2f;
    --gold: #c9a431;
    --gold-soft: #e2c15a;
    --ruby: #b5356a;
    --silver: #e4e1d8;
  }
  * { margin: 0; padding: 0; box-sizing: border-box; }
  html, body { width: 1200px; height: 404px; overflow: hidden; }
  body { background: var(--cream-light); }
  .banner {
    position: relative;
    width: 1200px;
    height: 404px;
    overflow: hidden;
    background: radial-gradient(ellipse 60% 90% at 58% 50%, var(--cream-light) 0%, var(--cream) 60%, var(--cream-deep) 100%);
  }
  .rule {
    position: absolute;
    left: 0;
    width: 100%;
    height: 3px;
    background: var(--rule);
  }
  .rule--top { top: 7px; }
  .rule--bottom { top: 393px; }

  .offer { position: absolute; left: 0; top: 0; width: 440px; height: 100%; }
  .offer__band {
    position: absolute;
    left: 0;
    top: 88px;
    width: 425px;
    height: 31px;
    background: linear-gradient(90deg, rgba(241,228,181,0) 0%, var(--band) 20%, var(--band) 100%);
  }
  .offer__eyebrow {
    position: absolute;
    left: 96px;
    top: 93px;
    font-family: "Montserrat", sans-serif;
    font-weight: 500;
    font-size: 19px;
    letter-spacing: 2.2px;
    color: var(--ink);
    white-space: nowrap;
  }
  .offer__headline {
    position: absolute;
    left: 95px;
    top: 146px;
    font-family: "Raleway", sans-serif;
    font-weight: 600;
    font-size: 48px;
    color: var(--ink);
    white-space: nowrap;
  }
  .offer__headline .offer__percent { color: var(--maroon); }
  .offer__sub {
    position: absolute;
    left: 97px;
    top: 206px;
    font-family: "Raleway", sans-serif;
    font-weight: 500;
    font-size: 31px;
    color: var(--ink);
    white-space: nowrap;
  }
  .offer__code {
    position: absolute;
    left: 92px;
    top: 262px;
    font-family: "Josefin Sans", sans-serif;
    font-weight: 300;
    font-size: 62px;
    letter-spacing: 3px;
    color: var(--gold);
    white-space: nowrap;
  }

  .product {
    position: absolute;
    border-radius: 45%;
  }
  .product--brooch {
    left: 540px; top: 32px; width: 300px; height: 345px;
    background: radial-gradient(circle at 52% 58%, var(--ruby) 0%, var(--ruby) 22%, var(--gold-soft) 40%, rgba(226,193,90,0.35) 70%, rgba(226,193,90,0) 100%);
  }
  .product--earrings {
    left: 880px; top: 38px; width: 220px; height: 150px;
    background: radial-gradient(ellipse at 50% 50%, var(--gold-soft) 0%, var(--gold) 45%, rgba(201,164,49,0.3) 75%, rgba(201,164,49,0) 100%);
  }
  .product--band-ring {
    left: 968px; top: 206px; width: 146px; height: 132px;
    background: radial-gradient(ellipse at 50% 50%, var(--silver) 0%, var(--gold-soft) 55%, rgba(226,193,90,0.3) 80%, rgba(226,193,90,0) 100%);
  }
</style>
</head>
<body>
  <div class="banner">
    <div class="rule rule--top"></div>
    <div class="rule rule--bottom"></div>

    <section class="offer">
      <div class="offer__band"></div>
      <p class="offer__eyebrow">MOTHER'S DAY SALE</p>
      <h1 class="offer__headline">Save <span class="offer__percent">15%</span></h1>
      <p class="offer__sub">with Promo Code:</p>
      <p class="offer__code">LOVEMOM</p>
    </section>

    <div class="product product--brooch" role="img" aria-label="Gold crab brooch set with pink sapphires and blue sapphire eyes"></div>
    <div class="product product--earrings" role="img" aria-label="Pair of gold rope earrings with diamond X crossovers"></div>
    <div class="product product--band-ring" role="img" aria-label="Gold and white gold openwork band ring"></div>
  </div>
</body>
</html>
```